Ridgeway Patrol Website Design

Hello Designers. I am an agency and am helping a security company get a better look. I have a new logo and a car done up. We are looking for a fresh look using the blue and the gold. Open to a complimentary color.

Here is the old site
https://moravanguard.com/

Here is another design for photos and everything. We weren't sold on it because we wanted to make it simple like the first one.

https://ww2.moravanguard.com/

Attached is also the copy I would like to put on there.

I am looking for tough, competent and simple. Our customers are contruction companies, event planners etc. It has to be clean and easy.

One thing we can't provide yet is photos. We are anticipating photos of our team with arms folded beside the car, close up of the owner with a logo'd shirt on. Pictures of an Ridgeway Patrol job site etc. (which most of the time is construction. They also do Mall security. You can see if you want to use stock photos for now.

I wanted to get the look of the front page done first. Hoping for something really awesome. Have fun.

```html
<!DOCTYPE html>
<html lang="en">
<head>
<meta charset="utf-8">
<title>Ridgeway Patrol — Security Professionals</title>
<link rel="stylesheet" href="https://fonts.googleapis.com/css2?family=Poppins:wght@400;500;600;700;800&display=swap">
<style>
:root{
  --gold:#8b6411;
  --gold-light:#a57a1c;
  --navy:#0e1d36;
  --navy-deep:#081427;
  --ink:#131a2a;
  --text:#555a66;
  --white:#ffffff;
  --line:#dcdcdc;
}
*{box-sizing:border-box;margin:0;padding:0}
html,body{width:1200px;height:4402px;overflow:hidden}
body{position:relative;font-family:'Poppins',sans-serif;color:var(--ink);background:var(--white)}
.abs{position:absolute}
.btn{position:absolute;display:flex;align-items:center;justify-content:center;gap:10px;background:var(--gold);color:var(--white);font-weight:700;font-size:14px;text-transform:uppercase;letter-spacing:.2px}
.btn .dot{width:15px;height:15px;border-radius:50%;background:var(--white);display:inline-flex;align-items:center;justify-content:center}
.btn .dot::after{content:"";border-left:5px solid var(--gold);border-top:3.5px solid transparent;border-bottom:3.5px solid transparent;margin-left:2px}
h2.title{position:absolute;font-size:32px;font-weight:700;text-transform:uppercase;line-height:1}

/* header */
.topline{left:0;top:0;width:1200px;height:5px;background:var(--ink)}
.site-header{left:0;top:5px;width:1200px;height:152px;background:var(--white);border-bottom:1px solid #e6e6e6}
.brand{position:absolute;display:flex;align-items:center;gap:8px;font-weight:800;color:var(--gold);text-transform:uppercase}
.header-phone{left:566px;top:32px;display:flex;align-items:center;gap:14px;font-size:30px;font-weight:700;color:var(--ink)}
.phone-badge{width:46px;height:46px;border-radius:50%;background:var(--gold);display:flex;align-items:center;justify-content:center}
.main-nav{left:360px;top:104px;width:727px;display:flex;justify-content:space-between;font-size:14px;font-weight:700;text-transform:uppercase}

/* hero */
.hero{left:0;top:157px;width:1200px;height:600px;background:linear-gradient(100deg,#0b1a33 0%,#0f2645 55%,#163456 100%)}
.hero-art{left:560px;top:0;width:640px;height:600px;background:radial-gradient(ellipse at 55% 45%,rgba(150,170,200,.35),rgba(20,45,80,0) 65%)}
.hero h1{position:absolute;left:111px;top:195px;font-size:58px;font-weight:700;line-height:1.18;color:var(--white);text-transform:uppercase}

/* schedule */
.schedule{left:0;top:757px;width:1200px;height:209px;background:var(--gold)}
.schedule h2{color:var(--white);left:0;width:1200px;text-align:center;top:46px}
.field{position:absolute;top:118px;height:41px;background:var(--white);font-size:14px;color:#333;padding:0 20px;display:flex;align-items:center;justify-content:space-between}
.schedule .btn{top:118px;left:894px;width:219px;height:41px;border:1.5px solid var(--white)}

/* about */
.about-photo{left:120px;top:1051px;width:435px;height:513px;background:linear-gradient(160deg,#6b5a7d,#1c1c22 55%,#b7a7b9);clip-path:polygon(5% 12%,32% 0,100% 13%,94% 52%,52% 100%,4% 50%)}
.about h2{left:598px;top:1092px}
.about p{position:absolute;left:598px;width:486px;font-size:13px;line-height:24px;color:var(--text)}

/* services */
.services-bg{left:0;top:1692px;width:1200px;height:709px;background:linear-gradient(180deg,#34384a,#262a3c 60%,#1f2233)}
.services h2{color:var(--white);left:0;width:1200px;text-align:center;top:1797px}
.card{position:absolute;top:1894px;width:323px;height:393px;background:var(--white);border-radius:6px}
.card .pic{position:absolute;left:8px;top:8px;width:307px;height:200px}
.card h3{position:absolute;top:238px;width:100%;text-align:center;font-size:17px;font-weight:700;text-transform:uppercase}
.card p{position:absolute;top:268px;left:30px;width:263px;text-align:center;font-size:13px;line-height:22px;color:var(--text)}
.card .btn{left:81px;top:365px;width:160px;height:43px;font-size:15px}

/* why */
.why h2{left:84px;top:2530px}
.why p.lead{position:absolute;left:84px;top:2598px;width:440px;font-size:13px;line-height:24px;color:var(--text)}
.feature{position:absolute;width:135px;height:135px;background:var(--white);border-radius:6px;box-shadow:0 0 10px rgba(0,0,0,.12);display:flex;flex-direction:column;align-items:center;justify-content:flex-end;padding-bottom:20px;text-align:center;font-size:11.5px;font-weight:700;line-height:16px;text-transform:uppercase}
.feature svg{margin-bottom:10px}
.why-accent{left:1043px;top:2970px;width:75px;height:73px;background:var(--gold)}
.why-photo{left:605px;top:2502px;width:499px;height:530px;background:linear-gradient(135deg,#8896a8,#3b4656 55%,#1b222c)}

/* contact */
.contact-left{left:0;top:3170px;width:600px;height:561px;background:var(--gold)}
.contact-right{left:600px;top:3170px;width:600px;height:561px;background:linear-gradient(180deg,#2a3043,#1b2132)}
.ghost{position:absolute;font-weight:700;text-transform:uppercase;color:rgba(255,255,255,.12);line-height:1}
.contact h2{left:132px;top:3320px;color:var(--white)}
.c-label{position:absolute;font-size:13px;font-weight:700;color:var(--white);text-transform:uppercase}
.c-value{position:absolute;font-size:19px;font-weight:700;color:var(--white);line-height:29px}
.c-icon{position:absolute;width:42px;height:42px;border-radius:50%;background:var(--white);display:flex;align-items:center;justify-content:center}
.f-field{position:absolute;border-bottom:1.5px solid rgba(255,255,255,.8);color:var(--white);font-size:13px;padding-bottom:8px}

/* cta */
.cta{left:0;top:3731px;width:1200px;height:268px;background:linear-gradient(180deg,#dfe2e6,#f1f2f4)}
.cta h2{left:0;width:1200px;text-align:center;top:3782px;font-size:38px;line-height:51px;color:var(--ink)}

/* footer */
.footer{left:0;top:3999px;width:1200px;height:354px;background:var(--gold);color:var(--white)}
.footer h4{position:absolute;top:4095px;font-size:21px;font-weight:700;text-transform:uppercase}
.f-link{position:absolute;left:417px;font-size:13px;font-weight:700;text-transform:uppercase}
.f-info{position:absolute;left:656px;font-size:12px;line-height:22px}
.social{position:absolute;top:4243px;width:28px;height:28px;border-radius:50%;background:var(--white)}
.copyright{left:0;top:4353px;width:1200px;height:49px;background:var(--ink);color:var(--white);font-size:15px;display:flex;align-items:center;justify-content:center}
</style>
</head>
<body>

<!-- Header -->
<div class="abs topline"></div>
<header class="abs site-header">
  <div class="brand" style="left:111px;top:46px;font-size:22px;line-height:1">
    <span style="width:18px;height:18px;background:var(--gold);display:block"></span>Ridgeway Patrol
  </div>
  <div class="abs header-phone">
    <span class="phone-badge"><svg width="22" height="22" viewBox="0 0 24 24"><path d="M6.6 10.8a15 15 0 006.6 6.6l2.2-2.2a1 1 0 011-.25 11.4 11.4 0 003.6.6 1 1 0 011 1V20a1 1 0 01-1 1A17 17 0 013 4a1 1 0 011-1h3.5a1 1 0 011 1c0 1.25.2 2.45.57 3.57a1 1 0 01-.25 1z" fill="#fff"/></svg></span>
    506.555.0142
  </div>
  <a class="btn" style="left:877px;top:24px;width:210px;height:44px">Request Services <span class="dot"></span></a>
  <nav class="abs main-nav">
    <span>Home</span><span>About</span><span>Careers</span><span>Services</span><span>Français</span><span>Testimonials</span><span>Contact Us</span>
  </nav>
</header>

<!-- Hero -->
<section class="abs hero">
  <div class="abs hero-art" role="img" aria-label="Dark blue technology backdrop with a large brand emblem"></div>
  <h1>Security<br>Professionals</h1>
  <a class="btn" style="left:113px;top:352px;width:212px;height:46px">Request Services <span class="dot"></span></a>
</section>

<!-- Schedule -->
<section class="abs schedule">
  <h2 class="title">Schedule Service Now</h2>
  <div class="field" style="left:87px;width:186px">Name</div>
  <div class="field" style="left:289px;width:186px">Email Address</div>
  <div class="field" style="left:490px;width:187px">Contact Number</div>
  <div class="field" style="left:692px;width:187px">Select Service <svg width="10" height="7" viewBox="0 0 10 7"><path d="M1 1l4 4 4-4" stroke="#333" stroke-width="1.6" fill="none"/></svg></div>
  <a class="btn" style="top:118px;left:894px;width:219px;height:41px">Schedule Service <span class="dot"></span></a>
</section>

<!-- About -->
<section class="about">
  <div class="abs about-photo" role="img" aria-label="Security officer in uniform speaking into a radio"></div>
  <h2 class="title">About Us</h2>
  <p style="top:1148px">We can meet any security need. Ridgeway Patrol is located in Dieppe, New Brunswick serving all of New Brunswick. We offer complete security services including event security, uniformed security and personal security services.</p>
  <p style="top:1268px">No detail will be overlooked. Our employee training and screening process ensures that we have the right people. Our professional employees are given the tools to succeed. From crowd control to protecting people and property, our team is trained with industry best practices.</p>
  <p style="top:1412px">We eliminate the guesswork for you by ensuring that we're up-to-date on all the regulations pertaining to public safety compliance.</p>
  <a class="btn" style="left:600px;top:1492px;width:164px;height:45px">Learn More <span class="dot"></span></a>
</section>

<!-- Service areas -->
<section class="services">
  <div class="abs services-bg" role="img" aria-label="Dimmed photo of security staff at work"></div>
  <svg class="abs" style="left:0;top:1680px" width="1200" height="100" viewBox="0 0 1200 100">
    <polygon points="0,0 1200,0 1200,82 600,20 0,82" fill="#fff"/>
    <polyline points="0,82 600,20 1200,82" fill="none" stroke="#8b6411" stroke-width="4"/>
    <circle cx="600" cy="20" r="14" fill="#fff" stroke="#8b6411" stroke-width="3"/>
    <circle cx="600" cy="20" r="5" fill="#8b6411"/>
  </svg>
  <h2 class="title">Service Areas</h2>
  <div class="card" style="left:73px">
    <div class="pic" role="img" aria-label="Event security guard facing a concert crowd" style="background:linear-gradient(135deg,#c04fd6,#3b2e7a 50%,#e0405a)"></div>
    <h3>Event Planners</h3>
    <p>There are many variations of passages of Lorem Ipsum available, but the majority have suffered</p>
    <a class="btn">Read More <span class="dot"></span></a>
  </div>
  <div class="card" style="left:439px">
    <div class="pic" role="img" aria-label="Construction workers on a rail site" style="background:linear-gradient(135deg,#6b7f99,#9a8a70 55%,#f0a040)"></div>
    <h3>Contruction Companies</h3>
    <p>There are many variations of passages of Lorem Ipsum available, but the majority have suffered</p>
    <a class="btn">Read More <span class="dot"></span></a>
  </div>
  <div class="card" style="left:805px">
    <div class="pic" role="img" aria-label="Security guard patrolling a shopping mall" style="background:linear-gradient(135deg,#8aa0a4,#5c6b5a 50%,#cfd6df)"></div>
    <h3>Mall Security</h3>
    <p>There are many variations of passages of Lorem Ipsum available, but the majority have suffered</p>
    <a class="btn">Read More <span class="dot"></span></a>
  </div>
</section>

<!-- Why choose us -->
<section class="why">
  <h2 class="title">Why Chose Us</h2>
  <p class="lead">It is a long established fact that a reader will be distracted by the readable content of a page when looking at its layout. The point of using Lorem Ipsum is that</p>

  <div class="feature" style="left:84px;top:2692px"><svg width="50" height="46" viewBox="0 0 50 46" fill="none" stroke="#8b6411" stroke-width="2"><circle cx="25" cy="14" r="6"/><circle cx="11" cy="19" r="5"/><circle cx="39" cy="19" r="5"/><path d="M14 44v-8a11 11 0 0122 0v8M2 44v-6a9 9 0 0112-8M48 44v-6a9 9 0 00-12-8"/></svg>Highly Trained<br>Team</div>
  <div class="feature" style="left:248px;top:2692px"><svg width="50" height="46" viewBox="0 0 50 46" fill="none" stroke="#8b6411" stroke-width="2"><circle cx="14" cy="12" r="6"/><circle cx="36" cy="12" r="6"/><path d="M4 44v-12a10 10 0 0120 0v12M26 44v-12a10 10 0 0120 0v12"/><path d="M20 30l5 4 5-4"/></svg>Trusted Security<br>Personals</div>
  <div class="feature" style="left:412px;top:2692px"><svg width="46" height="46" viewBox="0 0 46 46" fill="none" stroke="#8b6411" stroke-width="2"><path d="M13 10h20l-2 6H15z"/><circle cx="23" cy="22" r="7"/><path d="M8 45v-8a15 9 0 0130 0v8"/><path d="M18 38h10"/></svg>Events Security<br>Guards</div>
  <div class="feature" style="left:84px;top:2856px"><svg width="44" height="48" viewBox="0 0 44 48" fill="none" stroke="#8b6411" stroke-width="2"><circle cx="22" cy="24" r="20"/><rect x="14" y="22" width="16" height="12" rx="2"/><path d="M17 22v-4a5 5 0 0110 0v4"/></svg>High Quality<br>Services</div>
  <div class="feature" style="left:248px;top:2856px"><svg width="46" height="46" viewBox="0 0 46 46" fill="none" stroke="#8b6411" stroke-width="2"><circle cx="23" cy="17" r="8"/><path d="M11 17a12 12 0 0124 0M11 16v6M35 16v6M35 22c0 4-4 6-9 6"/><path d="M6 45v-6a17 11 0 0134 0v6"/></svg>Professional<br>Approach</div>
  <div class="feature" style="left:412px;top:2856px"><svg width="46" height="46" viewBox="0 0 46 46" fill="none" stroke="#8b6411" stroke-width="2"><path d="M14 12h18l-2 5H16z"/><circle cx="23" cy="23" r="7"/><path d="M16 23c-2 5-2 9 0 11M30 23c2 5 2 9 0 11"/><path d="M8 45v-6a15 9 0 0130 0v6"/></svg>Lady Security<br>Guards</div>

  <div class="abs why-accent"></div>
  <div class="abs why-photo" role="img" aria-label="Security officer at a monitoring desk speaking into a radio"></div>
</section>

<!-- Contact -->
<section class="contact">
  <div class="abs contact-left"></div>
  <div class="abs contact-right" role="img" aria-label="Dimmed photo of a security guard seen from behind"></div>
  <svg class="abs" style="left:0;top:3160px" width="1200" height="80" viewBox="0 0 1200 80">
    <polygon points="0,0 1200,0 1200,60 600,18 0,60" fill="#fff"/>
    <polyline points="0,60 600,18 1200,60" fill="none" stroke="#8b6411" stroke-width="4"/>
    <circle cx="600" cy="18" r="14" fill="#fff" stroke="#8b6411" stroke-width="3"/>
    <circle cx="600" cy="18" r="5" fill="#8b6411"/>
  </svg>
  <div class="ghost" style="left:128px;top:3308px;font-size:90px">Security</div>
  <div class="ghost" style="left:1043px;top:3300px;font-size:52px;color:rgba(255,255,255,.18)">Secur</div>
  <h2 class="title">Contact Us</h2>

  <div class="c-icon" style="left:133px;top:3420px"><svg width="22" height="22" viewBox="0 0 24 24"><path d="M6.6 10.8a15 15 0 006.6 6.6l2.2-2.2a1 1 0 011-.25 11.4 11.4 0 003.6.6 1 1 0 011 1V20a1 1 0 01-1 1A17 17 0 013 4a1 1 0 011-1h3.5a1 1 0 011 1c0 1.25.2 2.45.57 3.57a1 1 0 01-.25 1z" fill="none" stroke="#8b6411" stroke-width="1.6"/></svg></div>
  <div class="c-label" style="left:191px;top:3398px">Contact Number</div>
  <div class="c-value" style="left:191px;top:3418px">506.555.0142</div>

  <div class="c-icon" style="left:133px;top:3482px"><svg width="20" height="24" viewBox="0 0 20 24" fill="none" stroke="#8b6411" stroke-width="1.8"><path d="M10 23s8-8 8-13a8 8 0 00-16 0c0 5 8 13 8 13z"/><circle cx="10" cy="10" r="3"/></svg></div>
  <div class="c-label" style="left:191px;top:3462px">Location</div>
  <div class="c-value" style="left:191px;top:3482px">482 Rue Larchwood St.<br>Suite 204<br>Moncton NB<br>E1c 4h7</div>

  <div class="f-field" style="left:675px;top:3344px;width:183px">First Name</div>
  <div class="f-field" style="left:904px;top:3344px;width:183px">Last Name</div>
  <div class="f-field" style="left:675px;top:3401px;width:183px">Email Address</div>
  <div class="f-field" style="left:904px;top:3401px;width:183px">Contact Number</div>
  <div class="f-field" style="left:675px;top:3461px;width:412px">Message...</div>
  <a class="btn" style="left:921px;top:3527px;width:166px;height:45px">Send Mesage <span class="dot"></span></a>
</section>

<!-- CTA -->
<section class="abs cta" role="img" aria-label="Faded city skyline with a security guard"></section>
<h2 class="title" style="left:0;width:1200px;text-align:center;top:3782px;font-size:38px;line-height:51px">Day or night , 24/7 , count on trustedd<br>service from Ridgeway Patrol.</h2>
<div class="abs" style="left:342px;top:3904px;display:flex;align-items:center;gap:14px;font-size:30px;font-weight:700">
  <span class="phone-badge"><svg width="22" height="22" viewBox="0 0 24 24"><path d="M6.6 10.8a15 15 0 006.6 6.6l2.2-2.2a1 1 0 011-.25 11.4 11.4 0 003.6.6 1 1 0 011 1V20a1 1 0 01-1 1A17 17 0 013 4a1 1 0 011-1h3.5a1 1 0 011 1c0 1.25.2 2.45.57 3.57a1 1 0 01-.25 1z" fill="#fff"/></svg></span>
  506.555.0142
</div>
<a class="btn" style="left:650px;top:3903px;width:210px;height:45px">Request Services <span class="dot"></span></a>

<!-- Footer -->
<footer class="abs footer"></footer>
<div class="brand" style="left:150px;top:4150px;font-size:20px;color:var(--white)">
  <span style="width:16px;height:16px;background:var(--white);display:block"></span>Ridgeway Patrol
</div>
<span class="social" style="left:142px"></span>
<span class="social" style="left:184px"></span>
<span class="social" style="left:227px"></span>
<span class="social" style="left:270px"></span>

<h4 class="abs" style="left:417px;top:4095px;font-size:21px;font-weight:700;color:#fff;text-transform:uppercase">Quick Links</h4>
<span class="f-link" style="top:4140px;color:#fff">Home</span>
<span class="f-link" style="top:4170px;color:#fff">About Us</span>
<span class="f-link" style="top:4199px;color:#fff">Services</span>
<span class="f-link" style="top:4229px;color:#fff">Reviews</span>
<span class="f-link" style="top:4258px;color:#fff">Contact Us</span>

<h4 class="abs" style="left:622px;top:4095px;font-size:21px;font-weight:700;color:#fff;text-transform:uppercase">Find Us</h4>
<svg class="abs" style="left:624px;top:4142px" width="16" height="20" viewBox="0 0 16 20"><rect x="1" y="1" width="14" height="18" rx="2" fill="#fff"/><rect x="5" y="6" width="6" height="2" fill="#8b6411"/></svg>
<div class="f-info" style="top:4138px;color:#fff">482 RUE LARCHWOOD ST.<br>SUITE 204 , MONCTON NB ,E1C 4H7</div>
<svg class="abs" style="left:624px;top:4194px" width="16" height="16" viewBox="0 0 24 24"><path d="M6.6 10.8a15 15 0 006.6 6.6l2.2-2.2a1 1 0 011-.25 11.4 11.4 0 003.6.6 1 1 0 011 1V20a1 1 0 01-1 1A17 17 0 013 4a1 1 0 011-1h3.5a1 1 0 011 1c0 1.25.2 2.45.57 3.57a1 1 0 01-.25 1z" fill="#fff"/></svg>
<div class="f-info" style="top:4190px;color:#fff">506.555.0142</div>
<svg class="abs" style="left:623px;top:4229px" width="18" height="14" viewBox="0 0 18 14"><rect x="0" y="0" width="18" height="14" rx="1" fill="#fff"/><path d="M1 1l8 7 8-7" stroke="#8b6411" stroke-width="1.5" fill="none"/></svg>
<div class="f-info" style="top:4224px;color:#fff">info@ridgewaypatrol.com</div>

<h4 class="abs" style="left:861px;top:4095px;font-size:21px;font-weight:700;color:#fff;text-transform:uppercase">Sign Up</h4>
<div class="abs" style="left:863px;top:4146px;width:224px;height:43px;background:#fff;font-size:14px;color:#333;padding-left:20px;display:flex;align-items:center">Email Address</div>
<div class="abs" style="left:863px;top:4204px;width:224px;height:43px;background:#fff;font-size:14px;font-weight:700;color:var(--gold);display:flex;align-items:center;justify-content:center;gap:10px;text-transform:uppercase">Subscribe Now <span style="width:15px;height:15px;border-radius:50%;background:var(--gold);display:inline-block"></span></div>

<div class="abs copyright">Copyright © 2022 Ridgeway Patrol . All Rights Reserved.</div>

</body>
</html>
```